Broschüre
Zielgruppe
Wir sind eine ambulanter Pflegedienst in Rostock. Ab dem Herbst 25 bieten wir für Interessenten mit einem Pflegegrad begleitete reisen an. Eine Fachkraft wird Patienten mit Pflegegrad in kleinen Gruppen begleiten. Den Text für den Flyer haben wir eingefügt. Bitte die Bider aus dem Stock Portal wählen. Über den Flyer sollen Patienten gefunden werden.
Der Flyer
sollte Serios wirken und Reiselust der Senioren wecken.
Aufgabenstellung
Hier der Text für den Flyer:
Was wir bieten:
✔️ Begleitung durch erfahrene Pflegefachkräfte ✔️ Körperpflege, Medikamentengabe & Betreuung wie zuhause ✔️ 24-Stunden-Erreichbarkeit unserer Pflegekräfte vor Ort im gebuchten Hotel ✔️ Zusammenarbeit mit ausgewählten Hotels – barrierefrei & seniorengerecht ✔️ Kleine Gruppen & individuelle Betreuung vor Ort
Gut zu wissen:
Für unsere pflegerische Begleitung entstehen Ihnen keine zusätzlichen Kosten, wenn Sie einen Pflegegrad haben und das Verhinderungspflege-Budget noch nicht aufgebraucht ist.
Lediglich die Hotelkosten sind von Ihnen selbst zu tragen.
Wer hat Anspruch auf Verhinderungspflege?
Alle Pflegebedürftigen mit einem anerkannten Pflegegrad ab Stufe 2 können jährlich Verhinderungspflege über die Pflegekasse abrufen – ideal, um sich im Urlaub sicher begleiten zu lassen!
Unser Service – Ihr Mehrwert:
Wir organisieren Ihre Reise von A bis Z und begleiten Sie oder Ihre Angehörigen auf dem Weg zu Erholung und neuen Eindrücken – mit Herz, Kompetenz und Erfahrung. Vor Ort sind müssen Sie auf nichts verzichten und werden versorgt wie zu Hause. Gerne organisieren wir auch die Abholung aus ihrer Hässlichkeit.
???? Seniorenhafen Touren – Ihr verlässlicher Partner für Pflege und Lebensfreude
???? Jetzt informieren & Platz sichern: 0381 - 52794163
???? Mail@seniorenhafen-touren .de
???? www.seniorenhafen-touren.de

```html
<!DOCTYPE html>
<html lang="de">
<head>
<meta charset="utf-8">
<title>Seniorenhafen Touren – Flyer</title>
<link rel="stylesheet" href="https://fonts.googleapis.com/css2?family=Arimo:wght@400;700&display=swap">
<style>
  :root {
    --navy: #1b2550;
    --orange: #f47a20;
    --pale: #eef1f8;
    --brand-blue: #2f7fd8;
    --badge-top: #2b5aa8;
    --badge-bottom: #172557;
    --page: #e4e4e4;
    --paper: #ffffff;
  }
  * { margin: 0; padding: 0; box-sizing: border-box; }
  html, body {
    width: 1200px; height: 1200px; overflow: hidden;
    background: var(--page);
    font-family: "Arimo", Arial, sans-serif;
  }
  .flyer {
    position: absolute; left: 198px; top: 30px;
    width: 804px; height: 1140px;
    background: var(--paper); overflow: hidden;
  }
  .flyer-art { position: absolute; inset: 0; width: 804px; height: 1140px; }
  .brand {
    position: absolute; left: 68px; top: 46px;
    display: flex; align-items: center; gap: 20px;
  }
  .brand-dot {
    width: 98px; height: 98px; border-radius: 50%;
    background: var(--brand-blue);
  }
  .brand-name {
    font-weight: 700; font-size: 33px; color: var(--navy);
    letter-spacing: -0.3px;
  }
  .cta-badge {
    position: absolute; left: 747px; top: 546px;
    width: 206px; height: 206px;
    display: flex; flex-direction: column; align-items: center; justify-content: center;
    text-align: center; color: #fff; font-weight: 700;
  }
  .cta-text { font-size: 16px; line-height: 21px; margin-top: -14px; }
  .cta-phone { font-size: 20.5px; margin-top: 6px; }
  .headline {
    position: absolute; left: 90px; top: 660px;
    font-weight: 700; font-size: 53px; line-height: 67px;
    color: var(--navy); letter-spacing: -0.5px;
  }
  .accent { color: var(--orange); }
  .offer-title {
    position: absolute; left: 90px; top: 806px;
    font-weight: 700; font-size: 20px; color: #111;
  }
  .offer-list { position: absolute; left: 90px; top: 0; list-style: none; }
  .offer-item {
    position: absolute; left: 0; width: 640px;
    padding-left: 28px; font-size: 20.5px; line-height: 27px;
    color: var(--navy); white-space: nowrap;
  }
  .offer-item svg { position: absolute; left: 0; top: 5px; }
</style>
</head>
<body>
<main class="flyer">
  <svg class="flyer-art" viewBox="0 0 1290 1830" xmlns="http://www.w3.org/2000/svg">
    <defs>
      <linearGradient id="photoTone" x1="0" y1="0" x2="0" y2="1">
        <stop offset="0" stop-color="#f4ece2"/>
        <stop offset="0.35" stop-color="#b9c3c9"/>
        <stop offset="0.55" stop-color="#6c7456"/>
        <stop offset="0.75" stop-color="#8a4a2a"/>
        <stop offset="1" stop-color="#3e4230"/>
      </linearGradient>
      <linearGradient id="badgeTone" x1="0" y1="0" x2="0.6" y2="1">
        <stop offset="0" stop-color="var(--badge-top)"/>
        <stop offset="1" stop-color="var(--badge-bottom)"/>
      </linearGradient>
    </defs>
    <path class="decor-wave" fill="var(--pale)" d="M0 490 C180 450 320 450 420 470 L420 960 C300 970 200 1040 120 1070 C70 1085 30 1075 0 1070 Z"/>
    <path class="decor-blob" fill="var(--pale)" d="M1290 100 C1180 50 1130 110 1070 190 C1010 250 940 270 915 330 C890 420 930 520 1010 530 C1120 540 1220 470 1290 440 Z"/>
    <path role="img" aria-label="Foto: lachende Seniorin mit rotem Schal in herbstlicher Landschaft" fill="url(#photoTone)" d="M300 380 C420 180 700 40 950 110 C1080 150 1130 300 1150 480 C1180 650 1190 800 1110 880 L900 1005 C700 1015 450 1015 320 960 C200 900 150 760 160 650 C170 540 230 470 300 380 Z"/>
    <circle cx="1044" cy="984" r="165" fill="url(#badgeTone)"/>
  </svg>

  <div class="brand">
    <span class="brand-dot"></span>
    <span class="brand-name">Seniorenhafen Touren</span>
  </div>

  <div class="cta-badge">
    <p class="cta-text">Jetzt<br>informieren &amp;<br>einen Platz sichern:</p>
    <p class="cta-phone">0381 - 52794163</p>
  </div>

  <h1 class="headline">Pflege mit <span class="accent">Herz</span> –<br><span class="accent">Urlaub</span> mit Sicherheit</h1>

  <h2 class="offer-title">Was wir bieten:</h2>

  <ul class="offer-list">
    <li class="offer-item" style="top:846px"><svg width="20" height="22" viewBox="0 0 20 22"><path d="M2 12 L8 19 L18 2" fill="none" stroke="var(--orange)" stroke-width="3.5" stroke-linecap="round" stroke-linejoin="round"/></svg>Begleitung durch erfahrene Pflegefachkräfte</li>
    <li class="offer-item" style="top:884px"><svg width="20" height="22" viewBox="0 0 20 22"><path d="M2 12 L8 19 L18 2" fill="none" stroke="var(--orange)" stroke-width="3.5" stroke-linecap="round" stroke-linejoin="round"/></svg>Körperpflege, Medikamentengabe &amp; Betreuung wie zuhause</li>
    <li class="offer-item" style="top:922px"><svg width="20" height="22" viewBox="0 0 20 22"><path d="M2 12 L8 19 L18 2" fill="none" stroke="var(--orange)" stroke-width="3.5" stroke-linecap="round" stroke-linejoin="round"/></svg>24-Stunden-Erreichbarkeit unserer Pflegekräfte vor Ort<br>im gebuchten Hotel</li>
    <li class="offer-item" style="top:987px"><svg width="20" height="22" viewBox="0 0 20 22"><path d="M2 12 L8 19 L18 2" fill="none" stroke="var(--orange)" stroke-width="3.5" stroke-linecap="round" stroke-linejoin="round"/></svg>Zusammenarbeit mit ausgewählten Hotels –<br>barrierefrei &amp; seniorengerecht</li>
    <li class="offer-item" style="top:1052px"><svg width="20" height="22" viewBox="0 0 20 22"><path d="M2 12 L8 19 L18 2" fill="none" stroke="var(--orange)" stroke-width="3.5" stroke-linecap="round" stroke-linejoin="round"/></svg>Kleine Gruppen &amp; individuelle Betreuung vor Ort</li>
  </ul>
</main>
</body>
</html>
```